Apartment Brochure for Corvella Heights, Rockingham

We need a brochure prepared for a new apartment development in Rockingham.

We only require the template and first front pages and our in house designer can add the other pages and text as required.

Please provide brochure in Photoshop format with editable texts, and PDF format.

Brochure in A4 printable format.

Some of the text for brochure and all the illustrations can be found on the attached Powerpoint presentation.

The different sections of the brochure would be something like this:
1. The Development –
a. key information about the project (2 bedroom, priced from $355,000, quality finishings etc)
b. info on the amenities nearby (City park next door, shops across the road, beach down the road)
2. Why Invest in Rockingham - info on Rockingham
a. fast growing area of Western Australia
b. tourist hotspot
c. huge resource investment
d. good job opportunities
3. Development Plan & Floor Plan
4. About the Developer – Info about Beltor.

Feel free to contact me on 0417 586 921 or mervyn@beltor-example.com.au if you have any questions or require any further information. There is also the opportunity for more ongoing work!

Thank you!
Updates

Hello Everyone,

One page sample is fine at this stage. Please include Beltor logo, picture of apartments and the lake in the front of the brochure.

Photoshop version is preferred if you are successful in getting the job.

```html
<!DOCTYPE html>
<html lang="en">
<head>
<meta charset="utf-8">
<title>Corvella Heights – Brochure Cover</title>
<link rel="stylesheet" href="https://fonts.googleapis.com/css2?family=Cinzel:wght@400;700&display=swap">
<style>
  :root {
    --gold: #d8b98a;
    --ink: #3b2a1c;
    --sky-top: #9cc4e6;
    --sky-low: #dfe9f1;
    --building: #e7e4de;
    --lawn: #6f8a3f;
    --water: #4f86a8;
    --tree: #3f5a2c;
  }
  html, body {
    margin: 0;
    padding: 0;
    width: 849px;
    height: 1200px;
    overflow: hidden;
    background: var(--gold);
  }
  .cover {
    position: relative;
    width: 849px;
    height: 1200px;
    background: var(--gold);
    overflow: hidden;
  }
  .cover__art {
    position: absolute;
    inset: 0;
    display: block;
  }
  .brand {
    position: absolute;
    left: 310px;
    width: 229px;
    top: 975px;
    text-align: center;
    color: var(--ink);
    font-family: "Cinzel", serif;
  }
  .brand__mark {
    display: block;
    width: 26px;
    height: 26px;
    margin: 0 auto 14px;
    border-radius: 50%;
    background: var(--ink);
  }
  .brand__name {
    margin: 0;
    font-weight: 700;
    font-size: 40px;
    letter-spacing: 3px;
    line-height: 1;
  }
  .brand__tagline {
    margin: 10px 0 0;
    font-weight: 400;
    font-size: 15px;
    letter-spacing: 1.5px;
    line-height: 1.3;
  }
</style>
</head>
<body>
<main class="cover">
  <svg class="cover__art" width="849" height="1200" viewBox="0 0 849 1200" aria-hidden="false">
    <defs>
      <linearGradient id="apartmentsTone" x1="0" y1="0" x2="0" y2="1">
        <stop offset="0" stop-color="var(--sky-top)"/>
        <stop offset="0.45" stop-color="var(--building)"/>
        <stop offset="0.7" stop-color="#7e7f78"/>
        <stop offset="1" stop-color="#3d3e40"/>
      </linearGradient>
      <linearGradient id="fountainLakeTone" x1="0" y1="0" x2="0" y2="1">
        <stop offset="0" stop-color="var(--sky-top)"/>
        <stop offset="0.35" stop-color="var(--tree)"/>
        <stop offset="0.55" stop-color="var(--water)"/>
        <stop offset="1" stop-color="#2f6688"/>
      </linearGradient>
      <linearGradient id="birdLakeTone" x1="0" y1="0" x2="0" y2="1">
        <stop offset="0" stop-color="var(--sky-low)"/>
        <stop offset="0.3" stop-color="var(--water)"/>
        <stop offset="0.5" stop-color="var(--lawn)"/>
        <stop offset="1" stop-color="#5a7431"/>
      </linearGradient>
    </defs>

    <g class="photo photo--apartments" role="img" aria-label="Photo of the Corvella Heights apartment buildings with a paved driveway and landscaped gardens">
      <polygon points="0,0 849,0 849,130 424,690 0,130" fill="url(#apartmentsTone)"/>
    </g>

    <g class="photo photo--fountain-lake" role="img" aria-label="Photo of the city park lake with a fountain and trees">
      <polygon points="0,640 310,940 310,1200 0,1200" fill="url(#fountainLakeTone)"/>
    </g>

    <g class="photo photo--bird-lake" role="img" aria-label="Photo of the lake shore with water birds on the lawn and a fountain">
      <polygon points="849,640 539,940 539,1200 849,1200" fill="url(#birdLakeTone)"/>
    </g>
  </svg>

  <div class="brand">
    <span class="brand__mark" aria-hidden="true"></span>
    <p class="brand__name">BELTOR</p>
    <p class="brand__tagline">CREATING VALUE<br>SHARING VALUE</p>
  </div>
</main>
</body>
</html>
```